Neues Layout für ein Element auf der Homepage
Anselm hat unsere Wunschdesign sehr schön umgesetzt. Die Kommunikation mit ihm ist sehr entspannt und er zeigte sich auch bei mehreren Änderungswünschen kooperativ. Gerne wieder. :)
Zielgruppe
Die krugbote ist ein Getränkesofortlieferant. Der Grundgedanke hinter der krugbote ist es nach Bestellung die Getränke innerhalb von 120 Minuten kostenfrei bis an die Wohnungs-, Haustür oder ins Büro zu liefern. Dabei bestellen die Kunden Getränke auf der Webseite, um sie dann vor Ort geliefert zu bekommen.
Die Zielgruppe der krugbote ist daher breit gefächert. Sie umfasst alle Personen, die ihre Getränke in Mehrwegflaschen kaufen und online bestellen wollen. Die Zielgruppe umfasst u.a. Studenten, Berufstätige, Familien, Singlehaushalte, ältere Personen als auch Gewerbe, die Getränke ins Büro liefern lassen.
Aufgabenstellung
Für die neue Website der krugbote soll ein Element auf der Homepage umgestaltet werden. Dafür sollte die Anordnung von acht Text- sowie Bildelementen neugestaltet werden. Drei dieser Elemente sollte prominent dargestellt werden. Die Bild- und die Textelemente sind vorgegeben und befinden sich im Anhang.
Es sollte lediglich der Aufbau und die farbliche Gestaltung neu designt werden. Dabei ist es gewünscht, dass das neue Design zum Corporate Design passt (siehe Anhang).

```html
<!DOCTYPE html>
<html lang="de">
<head>
<meta charset="utf-8">
<title>Krugbote – Vorteile</title>
<link rel="stylesheet" href="https://fonts.googleapis.com/css2?family=Titillium+Web:wght@300;400;600;700&display=swap">
<style>
:root{
  --blue:#0d5a8f;
  --lime:#c5cf28;
  --frame:#cccccc;
  --text:#8c8c8c;
  --white:#ffffff;
  --dark:#333333;
}
*{margin:0;padding:0;box-sizing:border-box}
html,body{width:946px;height:1200px;overflow:hidden;background:var(--white)}
body{font-family:"Titillium Web",sans-serif;position:relative}
.abs{position:absolute}
.section-title{left:0;width:946px;top:50px;text-align:center;color:var(--blue);font-weight:700;font-size:14px}
.usp-icon{top:106px;width:161px;height:56px;display:flex;justify-content:center}
.usp-card{top:182px;width:161px}
.usp-card .tag{background:var(--lime);color:var(--white);font-weight:700;font-size:10px;text-align:center;height:18px;line-height:18px;position:relative;z-index:2;box-shadow:0 1px 0 #9aa020}
.usp-card .body{margin:-2px 4px 0;border:4px solid var(--frame);border-top:none;border-radius:0 0 9px 9px;color:var(--text);font-size:8.6px;line-height:11.4px;text-align:center;padding:4px 6px 6px}
.feature-band{left:7px;top:310px;width:938px;height:96px;background:var(--lime)}
.feature{top:334px;width:110px;text-align:center;color:var(--white)}
.feature svg{display:block;margin:0 auto 4px}
.feature span{font-size:7.5px;font-weight:600;text-transform:uppercase;letter-spacing:-.1px}
.brands-head{left:0;width:946px;top:414px;text-align:center}
.brands-head .rule{width:28px;height:2px;background:#e6e2c8;margin:0 auto 12px}
.brands-head h3{font-size:13px;font-weight:600;color:#666}
.brands-head small{display:block;font-size:7px;color:#bbb;margin-top:2px}
.carousel-arrow{left:8px;top:478px;width:32px;height:32px;border-radius:50%;background:#f4f4f4;color:#888;font-size:12px;display:flex;align-items:center;justify-content:center}
.brand{top:516px;width:96px;text-align:center;font-weight:700;font-size:17px;color:var(--blue)}
.brand.warm{color:#c7262f}
.brand.gold{color:#a88a3a}
.brand.faint{color:#ccc;width:30px}
.zoom{left:161px;top:600px;width:642px;height:470px;overflow:hidden}
.zoom .box-icon{left:138px;top:28px}
.zoom .card{left:46px;top:93px;width:258px}
.zoom .card .tag{background:var(--lime);color:var(--white);font-weight:700;font-size:17px;text-align:center;height:30px;line-height:30px;position:relative;z-index:2;box-shadow:0 2px 0 #9aa020}
.zoom .card .body{margin:-2px 4px 0;border:7px solid var(--frame);border-top:none;border-radius:0 0 16px 16px;color:var(--text);font-size:15px;line-height:18px;text-align:center;padding:6px 10px 10px}
.zoom .card.cut{left:-232px;top:93px}
.zoom .band{left:0;top:303px;width:642px;height:153px;background:var(--lime)}
.zoom .feat{top:340px;width:160px;text-align:center;color:var(--white);font-size:13px}
.zoom .feat svg{display:block;margin:0 auto 10px}
.zoom .feat.active{color:var(--blue)}
.popup{left:326px;top:202px;width:303px;height:184px;background:var(--white);border:7px solid var(--frame);border-radius:18px;text-align:center;padding:8px 14px}
.popup h4{color:var(--blue);font-size:19px;font-weight:700;margin-bottom:6px}
.popup p{color:var(--text);font-size:16.5px;line-height:21.5px;font-weight:300}
.cursor{left:253px;top:389px}
</style>
</head>
<body>

<h2 class="abs section-title">Das ist die Krugbote</h2>

<div class="abs usp-icon" style="left:257px">
  <svg width="48" height="56" viewBox="0 0 48 56" fill="none" stroke="var(--blue)" stroke-width="3.2"><circle cx="23" cy="31" r="18"/><circle cx="23" cy="31" r="11" stroke-width="2"/><path d="M19 8h8M23 8v5M37 15l4-4M23 31l-5 6" stroke-linecap="round"/></svg>
</div>
<div class="abs usp-icon" style="left:430px">
  <svg width="92" height="46" viewBox="0 0 92 46" fill="none" stroke="var(--blue)" stroke-width="3.4" stroke-linecap="round"><path d="M26 8h38c10 0 18 10 22 18v10h-8M58 36H40M26 36v-10"/><path d="M66 10v14h18"/><circle cx="34" cy="37" r="6"/><circle cx="72" cy="37" r="6"/><path d="M2 12h18M8 19h16M0 26h20M10 33h12"/></svg>
</div>
<div class="abs usp-icon" style="left:604px">
  <svg width="52" height="56" viewBox="0 0 52 56" fill="none" stroke="var(--blue)" stroke-width="3.2"><path d="M2 22h48v32H2z"/><path d="M10 30h32v14H10z"/><path d="M12 22V10l3-4V2h4v4l3 4v12M30 22V10l3-4V2h4v4l3 4v12"/></svg>
</div>

<div class="abs usp-card" style="left:257px">
  <div class="tag">LIEFERUNGEN IN 120 MINUTEN</div>
  <div class="body">Ab Ihrer Bestellung.<br>Immer und ohne Aufpreis!<br>Montag bis Samstag<br>9 bis 21 Uhr</div>
</div>
<div class="abs usp-card" style="left:430px">
  <div class="tag">KEINE LIEFERGEBÜHR</div>
  <div class="body">Alle Bestellungen erhalten<br>Sie kostenfrei bis an<br>Ihre Wohnungs- od.<br>Haustüre geliefert. Egal<br>in welchem Stockwerk<br>sich diese befindet.</div>
</div>
<div class="abs usp-card" style="left:604px">
  <div class="tag">BEQUEME PFANDRÜCKGABE</div>
  <div class="body">Ihr Leergut nehmen wir<br>ganz einfach wieder mit.<br>Der Pfandbetrag wird<br>dann direkt von der<br>Rechnung abgezogen.</div>
</div>

<div class="abs feature-band"></div>
<div class="abs feature" style="left:235px">
  <svg width="34" height="34" viewBox="0 0 34 34" fill="none" stroke="#fff" stroke-width="2"><path d="M18 3h12v12L15 30 3 18z"/><circle cx="24" cy="9" r="2"/><path d="M11 19l8-6M12 14h1M17 19h1"/></svg>
  <span>Günstige Preise</span>
</div>
<div class="abs feature" style="left:349px">
  <svg width="34" height="34" viewBox="0 0 34 34" fill="none" stroke="#fff" stroke-width="2"><rect x="4" y="10" width="26" height="18" rx="3"/><path d="M8 10l12-6 3 6M20 16h10v6H20z"/></svg>
  <span>Sicher bezahlen</span>
</div>
<div class="abs feature" style="left:463px">
  <svg width="36" height="34" viewBox="0 0 36 34" fill="none" stroke="#fff" stroke-width="2"><path d="M2 4h6l4 18h18l3-13H10M12 10h20M13 16h18M18 9v13M24 9v13"/><circle cx="15" cy="28" r="2.5"/><circle cx="27" cy="28" r="2.5"/></svg>
  <span>Geringer Mindestbestwert</span>
</div>
<div class="abs feature" style="left:577px">
  <svg width="34" height="34" viewBox="0 0 34 34" fill="none" stroke="#fff" stroke-width="2"><path d="M17 29L4 16C0 11 3 4 9 4c4 0 6 3 8 5 2-2 4-5 8-5 6 0 9 7 5 12z"/></svg>
  <span>Privat und Gewerbe</span>
</div>
<div class="abs feature" style="left:691px">
  <svg width="36" height="34" viewBox="0 0 36 34" fill="none" stroke="#fff" stroke-width="2"><rect x="2" y="14" width="8" height="16" rx="1"/><path d="M10 16l6-6 2-8c3 0 4 3 3 6l-1 4h10c2 0 3 2 2 4l-3 12c0 1-1 2-3 2H10"/></svg>
  <span>Freundbuch</span>
</div>

<div class="abs brands-head">
  <div class="rule"></div>
  <h3>Alle unsere Marken</h3>
  <small>alle anzeigen</small>
</div>
<div class="abs carousel-arrow">‹</div>
<div class="abs brand faint" style="left:208px">O</div>
<div class="abs brand gold" style="left:275px;font-size:15px">Brauhaus Kelm</div>
<div class="abs brand" style="left:389px">Teeblatt</div>
<div class="abs brand" style="left:503px">Orvia</div>
<div class="abs brand warm" style="left:617px">Sprudla</div>
<div class="abs brand faint" style="left:745px">V</div>

<div class="abs zoom">
  <svg class="abs box-icon" width="80" height="32" viewBox="0 0 80 32" fill="none" stroke="var(--blue)" stroke-width="4"><path d="M2 0v30h76V0"/><path d="M16 0v16h48V0"/></svg>

  <div class="abs card cut">
    <div class="tag">KEINE LIEFERGEBÜHR</div>
    <div class="body">x<br>x<br>x<br>x<br>x<br>x</div>
  </div>
  <div class="abs card">
    <div class="tag">BEQUEME PFANDRÜCKGABE</div>
    <div class="body">Ihr Leergut nehmen wir<br>ganz einfach wieder mit.<br>Der Pfandbetrag wird<br>dann direkt von der<br>Rechnung abgezogen.</div>
  </div>

  <div class="abs band"></div>
  <div class="abs feat" style="left:8px">
    <svg width="52" height="46" viewBox="0 0 52 46" fill="none" stroke="#fff" stroke-width="3.4"><path d="M26 42L6 22C0 14 5 3 14 3c6 0 9 4 12 8 3-4 6-8 12-8 9 0 14 11 8 19z"/></svg>
    PRIVAT UND GEWERBE
  </div>
  <div class="abs feat active" style="left:190px">
    <svg width="62" height="50" viewBox="0 0 62 50" fill="#fff" stroke="var(--blue)" stroke-width="3.4" stroke-linejoin="round"><rect x="3" y="22" width="14" height="24" rx="2"/><path d="M17 24l10-10 3-11c5 0 7 5 5 10l-2 6h17c4 0 6 3 5 6l-5 18c-1 2-2 3-5 3H17z"/></svg>
    FREUNDBUCH
  </div>

  <div class="abs popup">
    <h4>FREUNDBUCH</h4>
    <p>Folgen Sie uns auf Freundbuch und verpassen Sie keine Aktion! Unter allen Followern verlosen wir jeden Monat einen 100 Euro Einkaufsgutschein.</p>
  </div>

  <svg class="abs cursor" width="52" height="74" viewBox="0 0 52 74"><path d="M0 0v62l14-14 12 26 10-5-12-25h22z" fill="var(--dark)"/></svg>
</div>

</body>
</html>
```